Business Card Design Project

Name Martin Holroyd
Company Veldmark Site Restoration Crew
address 22/7 Penbrook street
Wattle Downs
Corvale Queensland
Australia 4187,
0498357261

Things that we do Mould inspection and Remediation,
Crime and Trauma Scene Cleanup and Decontamination
Drug lab Decontamination and needle cleanups.
Odor control
Air quality Testing and swabs,
latest equipment
Hydroxyl machines, ozone machines ,Sterilising lights ,Comercial Steam machines ,
Thermal imaging, Bacteria testing equipment
Fully trained personel

Reason: One day is not enough time to get designs i dont why the Current deadline is only one day

I do not need purovex in the cards, that was only a sample, The Business name isĀ 

Veldmark Site Restoration Crew.

Target Market(s)

Government agencies ,Police and real-estates, housing companies, Coroners

Industry/Entity Type

Business

Requirements
Must have
• Must tell what we are about
Nice to have
• raised letters or good background

```html
<!DOCTYPE html>
<html lang="en">
<head>
<meta charset="utf-8">
<title>Veldmark Site Restoration Crew – Business Cards</title>
<link href="https://fonts.googleapis.com/css2?family=Cinzel:wght@600&family=Questrial&display=swap" rel="stylesheet">
<style>
  :root {
    --page-bg: #ececec;
    --dark-top: #3a3a3a;
    --dark-mid: #141414;
    --dark-bottom: #000000;
    --dark-text: #ffffff;
    --dark-subtext: #e6e6e6;
    --light-top: #dcdcdc;
    --light-mid: #c4c4c4;
    --light-bottom: #a9a9a9;
    --light-name: #1e1e1e;
    --light-subtext: #4a4a4a;
    --brand-yellow: #f2e23a;
  }
  * { margin: 0; padding: 0; box-sizing: border-box; }
  html, body {
    width: 1200px;
    height: 1197px;
    overflow: hidden;
    background: var(--page-bg);
  }
  .business-card {
    position: absolute;
    left: 213px;
    width: 770px;
    height: 484px;
    border-radius: 26px;
    overflow: hidden;
    font-family: "Questrial", sans-serif;
  }
  .business-card--dark {
    top: 53px;
    background: radial-gradient(ellipse at 50% 30%, var(--dark-top) 0%, var(--dark-mid) 55%, var(--dark-bottom) 100%);
    color: var(--dark-subtext);
  }
  .business-card--light {
    top: 661px;
    background: radial-gradient(ellipse at 50% 30%, var(--light-top) 0%, var(--light-mid) 60%, var(--light-bottom) 100%);
    color: var(--light-subtext);
  }
  .card-sheen {
    position: absolute;
    inset: 0;
    width: 100%;
    height: 100%;
  }
  .brand-mark {
    position: absolute;
    left: 61px;
    top: 63px;
    width: 191px;
    display: flex;
    flex-direction: column;
    align-items: center;
    gap: 14px;
  }
  .brand-mark__dot {
    width: 120px;
    height: 120px;
    border-radius: 50%;
    background: var(--brand-yellow);
  }
  .brand-mark__name {
    font-size: 17px;
    line-height: 1.25;
    text-align: center;
    text-transform: uppercase;
    letter-spacing: 0.5px;
  }
  .business-card--dark .brand-mark__name { color: var(--dark-text); }
  .business-card--light .brand-mark__name { color: var(--light-name); }
  .holder-name {
    position: absolute;
    left: 445px;
    top: 56px;
    font-family: "Cinzel", serif;
    font-weight: 600;
    font-size: 34px;
    letter-spacing: 1px;
    font-variant: small-caps;
  }
  .business-card--dark .holder-name { color: var(--dark-text); }
  .business-card--light .holder-name { color: var(--light-name); }
  .holder-company {
    position: absolute;
    left: 445px;
    top: 103px;
    font-size: 21px;
    line-height: 28px;
  }
  .contact-phone {
    position: absolute;
    left: 61px;
    top: 300px;
    display: flex;
    align-items: center;
    gap: 24px;
    font-size: 24px;
  }
  .contact-phone svg { width: 26px; height: 22px; fill: currentColor; }
  .contact-address {
    position: absolute;
    left: 445px;
    top: 302px;
    font-size: 21px;
    line-height: 27.5px;
    font-style: normal;
  }
</style>
</head>
<body>

<section class="business-card business-card--dark">
  <svg class="card-sheen" viewBox="0 0 770 484" preserveAspectRatio="none" aria-hidden="true">
    <path d="M0 420 Q 300 200 770 190 L770 0 L0 0 Z" fill="#ffffff" opacity="0.05"/>
  </svg>
  <div class="brand-mark">
    <span class="brand-mark__dot"></span>
    <span class="brand-mark__name">Veldmark Site Restoration Crew</span>
  </div>
  <h1 class="holder-name">Martin Holroyd</h1>
  <p class="holder-company">Veldmark Site<br>Restoration Crew</p>
  <p class="contact-phone">
    <svg viewBox="0 0 26 22" aria-hidden="true"><path d="M2 7c0-3 5-5 11-5s11 2 11 5v2h-5V7H7v2H2z"/><path d="M5 11h16l2 9H3z"/><rect x="9" y="13" width="8" height="5" fill="#000" opacity="0.35"/></svg>
    0498357261
  </p>
  <address class="contact-address">22/7 Penbrook street<br>Wattle Downs<br>Corvale Queensland<br>Australia 4187</address>
</section>

<section class="business-card business-card--light">
  <svg class="card-sheen" viewBox="0 0 770 484" preserveAspectRatio="none" aria-hidden="true">
    <path d="M0 420 Q 300 200 770 190 L770 0 L0 0 Z" fill="#ffffff" opacity="0.18"/>
  </svg>
  <div class="brand-mark">
    <span class="brand-mark__dot"></span>
    <span class="brand-mark__name">Veldmark Site Restoration Crew</span>
  </div>
  <h2 class="holder-name">Martin Holroyd</h2>
  <p class="holder-company">Veldmark Site<br>Restoration Crew</p>
  <p class="contact-phone">
    <svg viewBox="0 0 26 22" aria-hidden="true"><path d="M2 7c0-3 5-5 11-5s11 2 11 5v2h-5V7H7v2H2z"/><path d="M5 11h16l2 9H3z"/><rect x="9" y="13" width="8" height="5" fill="#fff" opacity="0.45"/></svg>
    0498357261
  </p>
  <address class="contact-address">22/7 Penbrook street<br>Wattle Downs<br>Corvale Queensland<br>Australia 4187</address>
</section>

</body>
</html>
```